Esthetically Pleasing Core Values and Brand Promise for Accounting Firm

I would like a cohesive design that ties together my core values and brand promise. My firm, Maple Finch Advisory, provides accounting work to small businesses. I prefer modern and clean designs. I want my Core Values and Brand Promise to represent me - sole entrepreneur, married, mother of two kids, modern esthetics, clean lines, organized, colorful (teals, greys, white, yellows)

Industry/Entity Type

Public Accounting

Colors
33b8a4

```html
<!DOCTYPE html>
<html lang="en">
<head>
<meta charset="utf-8">
<title>Maple Finch Advisory — Core Values and Brand Promise</title>
<link rel="stylesheet" href="https://fonts.googleapis.com/css2?family=Arimo:wght@400;700&display=swap">
<style>
  :root {
    --teal-deep: #44acac;
    --teal-mid: #76c2c2;
    --teal-soft: #8dc3c5;
    --teal-light: #a5d6d6;
    --teal-pale: #cfe9e9;
    --teal-text: #3ca7a7;
    --white: #ffffff;
  }
  html, body {
    margin: 0;
    padding: 0;
    overflow: hidden;
    background: var(--white);
  }
  .canvas {
    width: 1200px;
    height: 1000px;
    position: relative;
    overflow: hidden;
    background: var(--white);
    font-family: "Arimo", Arial, sans-serif;
  }
  .diagram { display: block; }
  .divider { stroke: var(--white); stroke-width: 7; stroke-linejoin: round; }
  .seg-rectitude { fill: var(--teal-light); }
  .seg-relentless { fill: var(--teal-pale); }
  .seg-client { fill: var(--teal-mid); }
  .seg-empower { fill: var(--teal-deep); }
  .seg-trust, .seg-dependability { fill: var(--teal-soft); }
  .seg-transparency { fill: var(--teal-deep); }
  .seg-tax { fill: var(--teal-light); }
  .seg-accounting { fill: var(--teal-deep); }
  .hub { fill: var(--white); }
  .hub-disc { fill: var(--teal-deep); }

  .title { font-weight: 700; font-size: 16px; fill: var(--white); }
  .title--teal { fill: var(--teal-text); }
  .body { font-weight: 400; font-size: 10.5px; fill: var(--white); }
  .body--teal { fill: var(--teal-text); }
  .hub-label { font-weight: 700; font-size: 22px; fill: var(--teal-text); text-anchor: middle; }
  .promise-label { font-weight: 700; font-size: 17px; fill: var(--white); letter-spacing: 1px; }
  .brand-name { font-weight: 400; fill: var(--teal-text); text-anchor: middle; }
</style>
</head>
<body>
<main class="canvas">
  <svg class="diagram" width="1200" height="1000" viewBox="0 0 1200 1000" xmlns="http://www.w3.org/2000/svg">
    <defs>
      <linearGradient id="fade-left-wheel" x1="0" y1="0" x2="1" y2="0">
        <stop offset="0" stop-color="#44acac"/>
        <stop offset="1" stop-color="#44acac" stop-opacity="0"/>
      </linearGradient>
      <linearGradient id="fade-right-wheel" x1="1" y1="0" x2="0" y2="0">
        <stop offset="0" stop-color="#44acac"/>
        <stop offset="1" stop-color="#44acac" stop-opacity="0"/>
      </linearGradient>
      <path id="transparency-arc" d="M505 665 A165 165 0 0 0 695 665"/>
    </defs>

    <!-- Brand name -->
    <g class="brand">
      <text class="brand-name" x="600" y="245" font-size="34" letter-spacing="3">MAPLE FINCH</text>
      <text class="brand-name" x="600" y="282" font-size="20" letter-spacing="4">ADVISORY</text>
    </g>

    <!-- Core values wheel -->
    <g class="wheel wheel--values">
      <path class="seg-rectitude divider" d="M310 435 L181 251 A225 225 0 0 1 439 251 Z"/>
      <path class="seg-relentless divider" d="M310 435 L439 251 A225 225 0 0 1 526 497 Z"/>
      <path class="seg-client divider" d="M310 435 L94 497 A225 225 0 0 1 181 251 Z"/>
      <path class="seg-empower divider" d="M310 435 L310 660 A225 225 0 0 1 94 497 Z"/>
      <path class="divider" fill="url(#fade-left-wheel)" d="M310 435 L416 634 A225 225 0 0 1 310 660 Z"/>
      <circle class="hub" cx="310" cy="435" r="82"/>
      <text class="hub-label" x="312" y="425">CORE</text>
      <text class="hub-label" x="312" y="453">VALUES</text>

      <g class="value value--rectitude" text-anchor="middle">
        <text class="title" x="312" y="261">RECTITUDE</text>
        <text class="body" x="312" y="276">We know the difference</text>
        <text class="body" x="312" y="289">between what we have</text>
        <text class="body" x="312" y="302">the right to do and what</text>
        <text class="body" x="312" y="315">the right thing to do is.</text>
      </g>
      <g class="value value--client">
        <text class="title" x="115" y="363">CLIENT</text>
        <text class="title" x="115" y="385">FOCUSED</text>
        <text class="body" x="115" y="400">We provide a personal</text>
        <text class="body" x="115" y="413">service that goes</text>
        <text class="body" x="115" y="426">above the standards</text>
        <text class="body" x="115" y="439">of professional care.</text>
      </g>
      <g class="value value--empower">
        <text class="title" x="175" y="529">EMPOWER</text>
        <text class="body" x="175" y="544">We are dedicated,</text>
        <text class="body" x="175" y="557">appreciative and</text>
        <text class="body" x="175" y="570">respectful of people's</text>
        <text class="body" x="175" y="583">time and purpose.</text>
      </g>
      <g class="value value--relentless">
        <text class="title title--teal" x="390" y="366">RELENTLESS</text>
        <g text-anchor="end">
          <text class="body body--teal" x="505" y="381">We believe that the</text>
          <text class="body body--teal" x="505" y="394">longer we try to do</text>
          <text class="body body--teal" x="505" y="407">our best, the better</text>
          <text class="body body--teal" x="505" y="420">we become.</text>
        </g>
      </g>
    </g>

    <!-- Services wheel -->
    <g class="wheel wheel--services">
      <path class="seg-tax divider" d="M890 432 L675 498 A225 225 0 0 1 1022 250 Z"/>
      <path class="seg-accounting divider" d="M890 432 L1022 250 A225 225 0 0 1 890 657 Z"/>
      <path class="divider" fill="url(#fade-right-wheel)" d="M890 432 L890 657 A225 225 0 0 1 784 631 Z"/>
      <circle class="hub" cx="890" cy="432" r="80"/>
      <circle class="hub-disc" cx="890" cy="432" r="64"/>

      <g class="service service--tax">
        <text class="body" x="735" y="303">Maple Finch provides all clients with</text>
        <text class="body" x="735" y="316">a trusted tax advisor who provides</text>
        <text class="body" x="735" y="329">accuracy in all filings and ensures</text>
        <text class="body" x="735" y="342">your compliance with all</text>
        <text class="body" x="735" y="355">government agencies.</text>
        <text class="title" x="735" y="394">TAX</text>
      </g>
      <g class="service service--accounting">
        <text class="title" x="975" y="394" font-size="17">ACCOUNTING</text>
        <g text-anchor="end">
          <text class="body" x="1095" y="428">Maple Finch provides</text>
          <text class="body" x="1095" y="441">all business owners</text>
          <text class="body" x="1095" y="454">with the financial</text>
          <text class="body" x="1095" y="467">visibility needed to</text>
          <text class="body" x="1095" y="480">foster growth and</text>
          <text class="body" x="1095" y="493">facilitate goals.</text>
        </g>
      </g>
    </g>

    <!-- Brand promise arc -->
    <g class="wheel wheel--promise">
      <path class="seg-trust divider" d="M600 530 L463 705 A222 222 0 0 1 387 469 Z"/>
      <path class="seg-transparency divider" d="M600 530 L718 718 A222 222 0 0 1 482 718 Z"/>
      <path class="seg-dependability divider" d="M600 530 L813 469 A222 222 0 0 1 737 705 Z"/>
      <polygon class="seg-trust" points="436,478 476,490 452,504"/>
      <polygon class="seg-tax" points="742,456 724,482 768,478"/>
      <circle class="hub" cx="600" cy="530" r="82"/>
      <text class="hub-label" x="600" y="525" font-size="20">BRAND</text>
      <text class="hub-label" x="600" y="552" font-size="20">PROMISE</text>

      <text class="promise-label" text-anchor="middle" transform="translate(440 590) rotate(72)">TRUST</text>
      <text class="promise-label" text-anchor="middle">
        <textPath href="#transparency-arc" startOffset="50%">TRANSPARENCY</textPath>
      </text>
      <text class="promise-label" text-anchor="middle" transform="translate(760 580) rotate(-72)">DEPENDABILITY</text>
    </g>
  </svg>
</main>
</body>
</html>
```